Website for company called VORENTbio

We need a website for our new company called VORENTbio which developed a platform/technology to identify antigen-specific T cells (immune cells) which can be used for cancer therapy, autoimmunity, etc.

The platform is called VORENT and is rapid, versatile, unbiased, and inexpensive.

We have a semi-final logo although we are not completely set on color and font of text (attached).

Target Market(s)

Our target audience at the moment would be potential investors and VCs. We eventually are interested in getting attention from scientists and cell/immunotherapy companies.

Industry/Entity Type

Healthcare/Technology

Coding

Coded - Design and coding required

Number of Pages Required

1 page

Colors
0094D4
00A9DD
6FCCEA
C7EBF8
E9F6FB
00AB8E
00BBA5
67D7C9
C6EFE9
E9F9F6
E54698
E96AAD
F1A4CE
F9D9EA
FCEFF6
A7469A
B969AE
D3A5CF
EDDBEB
F8F0F9
6B429C
8869AF
B7A5CE
E3DAEB
F3F0F8

Requirements
Must have
• Landing page about the company, About us page, Technology page (could be merged with company landing page), Contact us page

```html
<!DOCTYPE html>
<html lang="en">
<head>
<meta charset="utf-8">
<title>VORENTbio — Targeted T Cell Discovery</title>
<link rel="stylesheet" href="https://fonts.googleapis.com/css2?family=Poppins:wght@500;600;700&family=Source+Sans+3:wght@400;600;700&display=swap">
<style>
:root{
  --blue:#0094D4;
  --blue-2:#00A9DD;
  --blue-3:#6FCCEA;
  --blue-4:#C7EBF8;
  --blue-5:#E9F6FB;
  --teal:#00AB8E;
  --teal-5:#E9F9F6;
  --ink:#111827;
  --text:#3b4656;
  --muted:#6b7584;
  --card:#f5f9fc;
  --white:#ffffff;
}
*{margin:0;padding:0;box-sizing:border-box}
html,body{width:1200px;height:3011px;overflow:hidden}
body{position:relative;background:var(--white);font-family:"Source Sans 3",sans-serif;color:var(--text)}
h1,h2,h3,h4,.brand{font-family:"Poppins",sans-serif;color:var(--ink)}
.abs{position:absolute}
.btn{display:inline-flex;align-items:center;justify-content:center;gap:8px;height:36px;border-radius:4px;font-family:"Source Sans 3",sans-serif;font-weight:600;font-size:10px;text-decoration:none}
.btn-primary{background:var(--blue);color:#fff}
.btn-ghost{background:#fff;color:var(--ink);border:1px solid #dfe7ee}

/* nav */
.site-nav{position:absolute;top:0;left:0;width:1200px;height:46px;background:var(--blue)}
.brand{display:flex;align-items:center;gap:6px;color:#fff;font-weight:600;font-size:17px;letter-spacing:-.2px}
.brand-dot{width:14px;height:14px;border-radius:50%;background:#fff}
.site-nav .brand{position:absolute;left:228px;top:12px}
.nav-links{position:absolute;right:216px;top:15px;display:flex;gap:20px;list-style:none}
.nav-links a{color:#e6f4fb;font-size:10.5px;text-decoration:none}
.nav-links a.active{color:#fff;font-weight:700}

/* hero */
.hero{position:absolute;top:46px;left:0;width:1200px;height:517px;background:linear-gradient(120deg,#eef7fd 0%,#e3f2fc 60%,#d8eefb 100%);overflow:hidden}
.hero-visual{position:absolute;top:0;left:0;width:1200px;height:517px;clip-path:polygon(710px 0,1200px 0,1200px 517px,664px 517px);background:radial-gradient(circle at 78% 30%,#cfe8f8 0%,#7fb6da 28%,#3f76a6 60%,#27517c 100%)}
.eyebrow{position:absolute;left:216px;top:40px;display:flex;align-items:center;gap:10px;font-size:8px;font-weight:700;color:var(--blue);letter-spacing:.4px}
.eyebrow::before{content:"";width:28px;height:1px;background:var(--blue)}
.hero h1{position:absolute;left:216px;top:76px;font-size:40px;line-height:43px;font-weight:700}
.hero h1 .accent{display:block;margin-top:10px;color:var(--blue);line-height:39px}
.hero-lead{position:absolute;left:216px;top:259px;width:430px;font-size:12px;line-height:20px;color:var(--text)}
.hero-actions{position:absolute;left:216px;top:316px;display:flex;gap:10px}
.hero-actions .btn-primary{width:145px}
.hero-actions .btn-ghost{width:99px}
.stats{position:absolute;left:216px;top:406px;display:flex;gap:40px}
.stat{text-align:center}
.stat b{display:block;font-family:"Poppins",sans-serif;font-weight:500;font-size:17px;color:var(--blue)}
.stat span{font-size:8px;color:var(--muted)}

/* mission */
.mission{position:absolute;top:605px;left:0;width:1200px;text-align:center}
.mission h2{font-size:23px;line-height:25px;font-weight:600}
.mission p{margin:28px auto 0;width:660px;font-size:10.5px;line-height:18px}

/* platform */
.platform{position:absolute;top:771px;left:0;width:1200px;height:306px}
.blob-left{position:absolute;left:0;top:0;width:160px;height:280px;border-radius:0 90px 90px 0;background:radial-gradient(circle at 30% 50%,#d6ecf8,#eaf5fb 70%,transparent 72%)}
.blob-right{position:absolute;right:0;top:130px;width:200px;height:176px;border-radius:100px 0 0 0;background:radial-gradient(circle at 70% 60%,#d6ecf8,#eaf5fb 70%,transparent 72%)}
.platform h2{position:absolute;left:216px;top:58px;font-size:22px;line-height:25px;font-weight:600}
.platform p{position:absolute;left:216px;top:128px;width:380px;font-size:10.5px;line-height:18px}
.platform .btn{position:absolute;left:216px;top:185px;width:142px}
.features{position:absolute;left:620px;top:21px;display:grid;grid-template-columns:174px 174px;gap:16px 16px}
.feature{height:110px;background:var(--card);border-radius:10px;padding:16px}
.feature-icon{width:28px;height:28px;border-radius:6px;background:var(--blue-4);display:flex;align-items:center;justify-content:center}
.feature-icon.teal{background:var(--teal-5)}
.feature h3{margin-top:14px;font-size:13px;font-weight:600}
.feature p{margin-top:10px;font-size:8.5px;color:var(--muted)}

/* use cases */
.use-cases{position:absolute;top:1077px;left:0;width:1200px;height:482px;background:var(--blue-5)}
.use-cases h2{position:absolute;top:49px;width:1200px;text-align:center;font-size:23px;font-weight:600}
.use-cases .sub{position:absolute;top:92px;width:1200px;text-align:center;font-size:10px}
.case-list{position:absolute;left:216px;top:127px;display:flex;gap:21px;align-items:center}
.case{width:242px;background:#fff;border-radius:10px;padding:20px}
.case-photo{width:202px;height:119px;border-radius:6px}
.ph-1{background:linear-gradient(135deg,#e7edf3,#a9bccd 60%,#7d93a8)}
.ph-2{background:linear-gradient(135deg,#1d5fb0,#1e88d8 55%,#0b2d6a)}
.ph-3{background:linear-gradient(135deg,#dfe7f5,#a8b9e6 55%,#7283c8)}
.case h3{margin-top:14px;font-size:15px;font-weight:500}
.case p{margin-top:12px;font-size:8.8px;line-height:16px;color:var(--muted)}
.case .btn{margin-top:12px;width:87px;height:27px;border-radius:3px}

/* investors */
.investors-band{position:absolute;top:1559px;left:0;width:1200px;height:286px;background:var(--blue)}
.investors-band h2{position:absolute;top:32px;width:1200px;text-align:center;color:#fff;font-size:23px;font-weight:600}
.investors-band p{position:absolute;top:66px;width:1200px;text-align:center;color:#eaf6fc;font-size:10.5px;line-height:18px}
.portrait-frame{position:absolute;left:345px;top:1680px;width:526px;height:331px;border-radius:22px;background:linear-gradient(180deg,var(--blue-2) 0%,#ffffff 55%);box-shadow:0 14px 34px rgba(10,40,80,.12);padding:14px}
.portrait{width:100%;height:100%;border-radius:14px;background:linear-gradient(160deg,#e9ecef,#c9d2da 55%,#9fb0bf)}
.reasons{position:absolute;top:2040px;left:216px;width:768px;display:grid;grid-template-columns:473px 295px;row-gap:16px}
.reason{display:flex;gap:9px}
.reason-icon{flex:none;width:18px;height:18px;border-radius:50%;background:var(--blue-5);display:flex;align-items:center;justify-content:center}
.reason-icon.teal{background:var(--teal-5)}
.reason h4{font-size:13px;font-weight:600}
.reason p{margin-top:5px;font-size:8.8px;color:var(--muted)}

/* contact */
.consult{position:absolute;top:2245px;left:214px;width:771px;height:552px;border-radius:28px;background:var(--blue-5);overflow:hidden}
.consult h2{position:absolute;left:43px;top:54px;font-size:25px;font-weight:500;color:var(--blue)}
.consult-form{position:absolute;left:43px;top:105px;width:419px;display:grid;grid-template-columns:200px 200px;gap:16px 19px}
.field{height:48px;border-radius:24px;background:#f4f9fc;display:flex;align-items:center;padding:0 27px;font-size:10.5px;color:#8d96a3}
.field.wide{grid-column:1/3;justify-content:space-between}
.field.message{grid-column:1/3;height:132px;align-items:flex-start;padding-top:22px;border-radius:24px}
.consult .btn{position:absolute;left:43px;top:462px;width:110px;height:40px;border-radius:20px;font-size:11px}
.consult-photo{position:absolute;right:0;top:68px;width:300px;height:484px;background:radial-gradient(ellipse at 60% 35%,#ffffff 0%,#eef3f6 50%,transparent 75%)}

/* footer */
.site-footer{position:absolute;top:2838px;left:0;width:1200px;height:173px;background:var(--ink)}
.site-footer .brand{position:absolute;left:216px;top:55px}
.footer-links{position:absolute;left:505px;top:63px;display:flex;gap:20px;list-style:none}
.footer-links a{color:#d6dbe3;font-size:9.5px;text-decoration:none}
.social{position:absolute;left:925px;top:55px;display:flex;gap:12px}
.social span{width:24px;height:24px;border-radius:50%;background:#273142;display:flex;align-items:center;justify-content:center}
.copyright{position:absolute;top:126px;width:1200px;text-align:center;font-size:9px;color:#8a93a3}
</style>
</head>
<body>

<nav class="site-nav">
  <div class="brand"><span class="brand-dot"></span>vorentbio</div>
  <ul class="nav-links">
    <li><a class="active" href="#">Home</a></li>
    <li><a href="#">About</a></li>
    <li><a href="#">Technology</a></li>
    <li><a href="#">Contact</a></li>
  </ul>
</nav>

<header class="hero">
  <div class="hero-visual" role="img" aria-label="Glowing blue T cell rendering floating in a laboratory"></div>
  <div class="eyebrow">NEXT-GEN IMMUNOTHERAPY</div>
  <h1>Revolutionizing<br>Immunotherapy with<span class="accent">Targeted T Cell<br>Discovery</span></h1>
  <p class="hero-lead">Meet VORENT – a fast, unbiased, and cost-effective platform identifying antigen-specific T cells for cancer, autoimmunity, and beyond.</p>
  <div class="hero-actions">
    <a class="btn btn-primary" href="#">Learn About VORENT
      <svg width="9" height="9" viewBox="0 0 10 10"><path d="M1 5h7M5 2l3 3-3 3" stroke="#fff" stroke-width="1.3" fill="none"/></svg></a>
    <a class="btn btn-ghost" href="#">Investor Brief</a>
  </div>
  <div class="stats">
    <div class="stat"><b>95%</b><span>Detection Rate</span></div>
    <div class="stat"><b>2hrs</b><span>Processing Time</span></div>
    <div class="stat"><b>50+</b><span>Partner Labs</span></div>
  </div>
</header>

<section class="mission">
  <h2>Transforming Immune Discovery for a<br>Healthier Future</h2>
  <p>At VORENTbio, we empower precision medicine through advanced T cell discovery. Our VORENT platform accelerates breakthroughs in immunotherapy—making them faster, more affordable, and accessible to scientists and developers globally.</p>
</section>

<section class="platform">
  <div class="blob-left" role="img" aria-label="Soft light blue cell cluster decoration"></div>
  <div class="blob-right" role="img" aria-label="Soft light blue cell cluster decoration"></div>
  <h2>A Next-Gen Platform to Decode<br>Immune Responses</h2>
  <p>VORENT is our proprietary tech that uncovers T cells specific to disease-driving antigens—offering unmatched immune insight.</p>
  <a class="btn btn-primary" href="#">Explore Our Technology</a>
  <div class="features">
    <div class="feature">
      <div class="feature-icon"><svg width="12" height="12" viewBox="0 0 12 12"><path d="M7 1L3 7h3l-1 4 4-6H6z" fill="none" stroke="#0094D4" stroke-width="1"/></svg></div>
      <h3>Rapid</h3><p>Results in hours</p>
    </div>
    <div class="feature">
      <div class="feature-icon teal"><svg width="12" height="12" viewBox="0 0 12 12"><path d="M2.5 6a3.5 3.5 0 0 1 6-2.4M9.5 6a3.5 3.5 0 0 1-6 2.4M8.5 1.5v2h-2M3.5 10.5v-2h2" fill="none" stroke="#00AB8E" stroke-width="1"/></svg></div>
      <h3>Versatile</h3><p>Works across diseases</p>
    </div>
    <div class="feature">
      <div class="feature-icon"><svg width="12" height="12" viewBox="0 0 12 12"><circle cx="5" cy="5" r="3.3" fill="none" stroke="#0094D4" stroke-width="1.1"/><path d="M7.5 7.5L10.5 10.5" stroke="#0094D4" stroke-width="1.2"/></svg></div>
      <h3>Unbiased</h3><p>No prior assumptions</p>
    </div>
    <div class="feature">
      <div class="feature-icon teal"><svg width="12" height="12" viewBox="0 0 12 12"><circle cx="6" cy="6" r="4.5" fill="none" stroke="#00AB8E" stroke-width="1"/><path d="M6 3.5v5M7.3 4.6H5.4a.9.9 0 0 0 0 1.8h1.2a.9.9 0 0 1 0 1.8H4.7" fill="none" stroke="#00AB8E" stroke-width=".9"/></svg></div>
      <h3>Cost-Effective</h3><p>Scalable &amp; efficient</p>
    </div>
  </div>
</section>

<section class="use-cases">
  <h2>Engineered for Real-World Immunotherapy</h2>
  <p class="sub">VORENT meets the needs of biotech, pharma, and academia aiming to leverage immune responses.</p>
  <div class="case-list">
    <article class="case">
      <div class="case-photo ph-1" role="img" aria-label="Scientist working at microscopes in a bright lab"></div>
      <h3>Cancer Immunotherapy</h3>
      <p>Target tumor-specific T cells for breakthrough cancer treatments and personalized therapy approaches.</p>
      <a class="btn btn-primary" href="#">View More</a>
    </article>
    <article class="case">
      <div class="case-photo ph-2" role="img" aria-label="Researchers at microscopes in a blue-lit laboratory"></div>
      <h3>Autoimmune Research</h3>
      <p>Map immune overactivation patterns to develop targeted treatments for autoimmune conditions.</p>
      <a class="btn btn-primary" href="#">View More</a>
    </article>
    <article class="case">
      <div class="case-photo ph-3" role="img" aria-label="Modern cell therapy laboratory with equipment"></div>
      <h3>Cell Therapy</h3>
      <p>Improve TCR &amp; CAR-T engineering with precise T cell identification and characterization.</p>
      <a class="btn btn-primary" href="#">View More</a>
    </article>
  </div>
</section>

<section class="investors-band">
  <h2>Why Investors Are Watching</h2>
  <p>With a patent-pending platform and scalable pipeline, VORENTbio sits at the<br>crossroads of science and technology.</p>
</section>
<div class="portrait-frame"><div class="portrait" role="img" aria-label="Smiling doctor in a white coat seated at a desk"></div></div>
<div class="reasons">
  <div class="reason">
    <span class="reason-icon"><svg width="9" height="9" viewBox="0 0 10 10"><path d="M5 1c2 1.5 2 4.5 1.2 6.5H3.8C3 5.5 3 2.5 5 1z" fill="none" stroke="#0094D4" stroke-width=".9"/></svg></span>
    <div><h4>Fast-tracked Development</h4><p>Accelerated timeline from discovery to clinical application</p></div>
  </div>
  <div class="reason">
    <span class="reason-icon"><svg width="9" height="9" viewBox="0 0 10 10"><path d="M1 9h8M2 7l2.5-2.5 2 1.5L9 3" fill="none" stroke="#0094D4" stroke-width=".9"/></svg></span>
    <div><h4>Expanding Immunotherapy Market</h4><p>Multi-billion dollar market opportunity with growing demand</p></div>
  </div>
  <div class="reason">
    <span class="reason-icon teal"><svg width="9" height="9" viewBox="0 0 10 10"><circle cx="5" cy="5" r="3.5" fill="none" stroke="#00AB8E" stroke-width=".9"/></svg></span>
    <div><h4>Patent-pending Technology</h4><p>Protected intellectual property with competitive advantages</p></div>
  </div>
  <div class="reason">
    <span class="reason-icon teal"><svg width="9" height="9" viewBox="0 0 10 10"><circle cx="3.5" cy="3.5" r="1.3" fill="none" stroke="#00AB8E" stroke-width=".9"/><circle cx="6.5" cy="3.5" r="1.3" fill="none" stroke="#00AB8E" stroke-width=".9"/><path d="M1.5 8.5c0-2 4-2 4 0M4.5 8.5c0-2 4-2 4 0" fill="none" stroke="#00AB8E" stroke-width=".9"/></svg></span>
    <div><h4>Proven Scientific Leadership</h4><p>World-class team with track record in immunology and biotech</p></div>
  </div>
</div>

<section class="consult">
  <div class="consult-photo" role="img" aria-label="Smiling doctor with stethoscope pointing toward the form"></div>
  <h2>Book A Free Consultation</h2>
  <form class="consult-form">
    <div class="field">First Name</div>
    <div class="field">Last Name</div>
    <div class="field">Email ID</div>
    <div class="field">Mobile Number</div>
    <div class="field wide">Country <svg width="8" height="8" viewBox="0 0 8 8"><path d="M1.5 3l2.5 2.5L6.5 3" fill="none" stroke="#555" stroke-width="1"/></svg></div>
    <div class="field message">Message</div>
  </form>
  <a class="btn btn-primary" href="#">Submit</a>
</section>

<footer class="site-footer">
  <div class="brand"><span class="brand-dot"></span>vorentbio</div>
  <ul class="footer-links">
    <li><a href="#">Home</a></li>
    <li><a href="#">About</a></li>
    <li><a href="#">Technology</a></li>
    <li><a href="#">Contact</a></li>
  </ul>
  <div class="social">
    <span><svg width="10" height="10" viewBox="0 0 10 10"><rect x="1" y="2" width="8" height="6" rx="1" fill="none" stroke="#d6dbe3" stroke-width=".9"/><path d="M1.3 2.5L5 5.5l3.7-3" fill="none" stroke="#d6dbe3" stroke-width=".9"/></svg></span>
    <span></span>
  </div>
  <p class="copyright">© 2025 VORENTbio. All rights reserved.</p>
</footer>

</body>
</html>
```